Business Card Design

- one on one personal training
- group personal training
- indoor or outdoor training available
- fitness and health assessments
- personalised fitness programs
- flexible hours for training

I am a Personal Trainer in Perth Australia. I am looking to expand my word of mouth client base.

I would like to see something that uses the colours blue, green and/or yellow.

The final design should reflect the way that I train clients, fun, motivating and perhaps a little quirky?
Updates

update with a logo with the letters MPT thank you

Hi all, Have had some great designs so far. Have decided to go double sided, perhaps to use the back to list my services. Thank you

Please check update brief. Thank you.

Target Market(s)

Professionals, ages 30 to 60

Industry/Entity Type

Training

Contact Information for Business Card

Mira Ostrowski
Personal Trainer

0491 570 118
mirapersonaltrainer@quillnest.com
http://www.mirapersonaltrainer.net

Requirements
Must have
• A logo with the letter MPT
Nice to have
• a logo to represent either; fitness, health, change, overall well-being.
Should not have
• Please no weights or lotus flowers!!

```html
<!DOCTYPE html>
<html lang="en">
<head>
<meta charset="utf-8">
<title>Mira Ostrowski – Personal Trainer Business Card</title>
<link rel="stylesheet" href="https://fonts.googleapis.com/css2?family=PT+Sans+Narrow:wght@400;700&family=Open+Sans:wght@400;600&display=swap">
<style>
  :root {
    --backdrop: #161616;
    --card: #ffffff;
    --ink: #111111;
    --teal: #1fdc8a;
    --orange: #f7931e;
    --yellow: #ffcc00;
    --green: #6fe000;
    --blue: #2e93f2;
    --logo-blue: #1f4fd8;
  }
  * { margin: 0; padding: 0; box-sizing: border-box; }
  html, body {
    width: 1200px;
    height: 824px;
    overflow: hidden;
    background: var(--backdrop);
  }
  .card {
    position: absolute;
    left: 40px;
    top: 82px;
    width: 1120px;
    height: 660px;
    background: var(--card);
    overflow: hidden;
    font-family: "Open Sans", Arial, sans-serif;
    color: var(--ink);
  }
  .card__accent {
    position: absolute;
    left: 0;
    right: 0;
    bottom: 0;
    height: 64px;
    background: linear-gradient(90deg, var(--blue) 0%, var(--green) 55%, var(--yellow) 100%);
  }
  .brand {
    position: absolute;
    left: 200px;
    top: 110px;
    display: flex;
    align-items: center;
    gap: 14px;
  }
  .brand__dot {
    width: 26px;
    height: 26px;
    border-radius: 50%;
    background: var(--green);
  }
  .brand__name {
    font-family: "PT Sans Narrow", Arial, sans-serif;
    font-weight: 700;
    font-size: 84px;
    line-height: 1;
    color: var(--logo-blue);
  }
  .identity {
    position: absolute;
    left: 110px;
    top: 262px;
    width: 420px;
    text-align: center;
  }
  .identity__name {
    font-family: "PT Sans Narrow", Arial, sans-serif;
    font-weight: 700;
    font-size: 58px;
    line-height: 1.1;
    letter-spacing: -0.5px;
  }
  .identity__role {
    font-size: 28px;
    margin-top: 2px;
  }
  .identity__phone {
    font-size: 27px;
    margin-top: 30px;
  }
  .contact {
    position: absolute;
    left: 95px;
    top: 486px;
    font-size: 26px;
    line-height: 1.45;
    font-style: normal;
  }
  .services {
    position: absolute;
    left: 585px;
    top: 238px;
    list-style: none;
    font-size: 25px;
    line-height: 1.65;
  }
  .services__item {
    display: flex;
    align-items: center;
    gap: 20px;
  }
  .services__item::before {
    content: "";
    width: 18px;
    height: 18px;
    border-radius: 50%;
    background: var(--dot);
    flex: none;
  }
  .services__item--teal   { --dot: var(--teal); }
  .services__item--orange { --dot: var(--orange); }
  .services__item--yellow { --dot: var(--yellow); }
  .services__item--green  { --dot: var(--green); }
  .services__item--blue   { --dot: var(--blue); }
</style>
</head>
<body>
  <main class="card">
    <div class="card__accent" role="img" aria-label="Decorative layered colour band in blue, green and yellow along the bottom edge"></div>

    <div class="brand">
      <span class="brand__dot"></span>
      <span class="brand__name">MPT</span>
    </div>

    <section class="identity">
      <h1 class="identity__name">Mira Ostrowski</h1>
      <p class="identity__role">Personal Trainer</p>
      <p class="identity__phone">Phone : 0491 570 118</p>
    </section>

    <ul class="services">
      <li class="services__item services__item--teal">One on one personal training</li>
      <li class="services__item services__item--orange">Group personal training</li>
      <li class="services__item services__item--yellow">Indoor or outdoor training available</li>
      <li class="services__item services__item--green">Fitness and health assessments</li>
      <li class="services__item services__item--blue">Personalised fitness programs</li>
    </ul>

    <address class="contact">
      E-mail: mirapersonaltrainer@quillnest.com<br>
      Website: www.mirapersonaltrainer.net
    </address>
  </main>
</body>
</html>
```